Data Analytics Irish company needs Stationery Design

We need a stationery design for our data analytics company based in Dublin called 'Quorbeam': we develop innovative web-based corporate applications exploiting advanced Machine Learning and Data Mining techniques.
Like the animal that inspired our company name, the final design should communicate intelligence and passion; on the other hand, we want to keep the highest professional appeal.
We love our current logo and we have tried out several color variations: we prefer solutions (see the logo attached) with white design and dark backgrounds, but we will also be glad to see some designs that follow the colors of the palette of the attached web screenshot.
It Company

```html
<!DOCTYPE html>
<html lang="en">
<head>
<meta charset="utf-8">
<title>Quorbeam Stationery</title>
<link rel="stylesheet" href="https://fonts.googleapis.com/css2?family=Montserrat:wght@400;600&display=swap">
<style>
  :root{
    --backdrop:#e9e9ea;
    --paper:#f4f4f5;
    --ink:#1f2229;
    --ink-soft:#2a2e36;
    --mark-faint-light:#e2e2e4;
    --mark-faint-dark:#272b33;
    --text-grey:#6b6e74;
    --accent:#5b7fb8;
    --shadow:0 6px 14px rgba(0,0,0,.14);
  }
  *{box-sizing:border-box;margin:0;padding:0}
  html,body{width:1200px;height:877px;overflow:hidden}
  body{background:var(--backdrop);font-family:"Montserrat",sans-serif;position:relative}
  .piece{position:absolute;box-shadow:var(--shadow);overflow:hidden}
  .paper{background:var(--paper)}
  .dark{background:var(--ink)}

  .brand{display:flex;align-items:center;gap:6px;font-weight:600;letter-spacing:-.2px;line-height:1}
  .brand .dot{border-radius:50%;flex:none}
  .on-light{color:var(--ink)}
  .on-light .dot{background:var(--ink)}
  .on-dark{color:#fff}
  .on-dark .dot{background:#fff}

  .faint-circle{position:absolute;border-radius:50%}
  .paper .faint-circle{background:var(--mark-faint-light)}
  .dark .faint-circle{background:var(--mark-faint-dark)}

  .small-print{font-size:5px;color:var(--text-grey);line-height:1.5}
  .contact-row{display:flex;align-items:center;gap:3px}
  .contact-icon{width:5px;height:5px;border-radius:50%;background:var(--accent);flex:none}

  /* letterhead */
  .letterhead{left:40px;top:50px;width:310px;height:438px}
  .letterhead .brand{position:absolute;left:26px;top:30px;font-size:17px}
  .letterhead .brand .dot{width:15px;height:15px}
  .letterhead .faint-circle{right:20px;bottom:70px;width:70px;height:70px}
  .letterhead .footer{position:absolute;left:26px;right:26px;bottom:22px;display:flex;gap:18px}

  /* folder */
  .folder{left:370px;top:50px;width:310px;height:438px}
  .folder .brand{position:absolute;left:26px;top:30px;font-size:17px}
  .folder .brand .dot{width:15px;height:15px}
  .folder .web{position:absolute;left:48px;top:52px;font-size:6px;color:#9a9ea6}
  .folder .faint-circle{right:-40px;top:120px;width:260px;height:260px}

  /* envelope */
  .envelope{left:700px;top:50px;width:450px;height:220px}
  .envelope .flap{position:absolute;left:0;top:0;right:0;height:58px;background:var(--ink);display:flex;align-items:center;justify-content:center}
  .envelope .flap .dot{width:16px;height:16px;border-radius:50%;background:#fff}

  /* compliment slip */
  .slip{left:700px;top:290px;width:450px;height:200px}
  .slip .brand{position:absolute;left:28px;top:84px;font-size:19px}
  .slip .brand .dot{width:17px;height:17px}
  .slip .faint-circle{right:24px;top:18px;width:110px;height:110px}
  .slip .address{position:absolute;right:28px;bottom:18px}

  /* business cards */
  .card{width:252px;height:144px}
  .card-back{left:40px;top:520px}
  .card-back .brand{position:absolute;left:18px;top:22px;font-size:14px}
  .card-back .brand .dot{width:12px;height:12px}
  .card-back .faint-circle{right:16px;top:14px;width:50px;height:50px}
  .card-back .person{position:absolute;left:18px;bottom:22px}
  .card-back .person-name{font-size:7px;font-weight:600;color:var(--ink);margin-bottom:2px}
  .card-back .details{position:absolute;right:18px;bottom:22px}
  .card-front{left:310px;top:520px;display:flex;align-items:center;justify-content:center}
  .card-front .brand{font-size:18px}
  .card-front .brand .dot{width:15px;height:15px}

  /* notebook */
  .notebook{left:590px;top:520px;width:220px;height:300px}
  .notebook .brand{position:absolute;left:34px;top:26px;font-size:16px}
  .notebook .brand .dot{width:14px;height:14px}
  .notebook .faint-circle{right:-30px;bottom:20px;width:170px;height:170px}
  .spiral{position:absolute;left:8px;top:12px;bottom:12px;width:10px;display:flex;flex-direction:column;justify-content:space-between}
  .spiral span{display:block;height:3px;border-radius:2px;background:#8d9098}

  /* keychain */
  .keyring{position:absolute;left:880px;top:528px;width:22px;height:22px;border:2px solid #a9acb2;border-radius:50%}
  .keychain{left:850px;top:552px;width:84px;height:56px;border-radius:8px;display:flex;align-items:center;justify-content:center;border:3px solid #d0d2d6}
  .keychain .brand{font-size:10px;gap:3px}
  .keychain .brand .dot{width:8px;height:8px}

  /* pencils */
  .pencil{position:absolute;height:9px;width:230px;background:var(--ink-soft);border-radius:0 2px 2px 0;box-shadow:var(--shadow)}
  .pencil::before{content:"";position:absolute;left:-16px;top:0;border-right:16px solid #c9b08a;border-top:4.5px solid transparent;border-bottom:4.5px solid transparent}
  .pencil-one{left:980px;top:560px}
  .pencil-two{left:980px;top:590px}

  /* eraser */
  .eraser{left:850px;top:640px;width:120px;height:40px;display:flex;align-items:center;justify-content:center;border-radius:3px}
  .eraser .brand{font-size:12px;gap:4px}
  .eraser .brand .dot{width:9px;height:9px}
</style>
</head>
<body>

<section class="piece paper letterhead">
  <div class="brand on-light"><span class="dot"></span>Quorbeam</div>
  <div class="faint-circle"></div>
  <div class="footer small-print">
    <div>Harbour Court<br>Ringsend, Dublin 4</div>
    <div>
      <div class="contact-row"><span class="contact-icon"></span>01 555 0142</div>
      <div class="contact-row"><span class="contact-icon"></span>01 555 0143</div>
    </div>
    <div>
      <div class="contact-row"><span class="contact-icon"></span>info@quorbeam.com</div>
      <div class="contact-row"><span class="contact-icon"></span>www.quorbeam.com</div>
    </div>
  </div>
</section>

<section class="piece dark folder">
  <div class="faint-circle"></div>
  <div class="brand on-dark"><span class="dot"></span>Quorbeam</div>
  <div class="web">www.quorbeam.com</div>
</section>

<section class="piece paper envelope">
  <div class="flap"><span class="dot"></span></div>
</section>

<section class="piece paper slip">
  <div class="faint-circle"></div>
  <div class="brand on-light"><span class="dot"></span>Quorbeam</div>
  <div class="address small-print">Harbour Court, Ringsend, Dublin 4</div>
</section>

<section class="piece paper card card-back">
  <div class="brand on-light"><span class="dot"></span>Quorbeam</div>
  <div class="faint-circle"></div>
  <div class="person small-print">
    <div class="person-name">NIAMH KEOGH</div>
    <div>Managing Director</div>
    <div>Harbour Court, Dublin 4</div>
  </div>
  <div class="details small-print">
    <div class="contact-row"><span class="contact-icon"></span>01 555 0142</div>
    <div class="contact-row"><span class="contact-icon"></span>niamh@quorbeam.com</div>
    <div class="contact-row"><span class="contact-icon"></span>www.quorbeam.com</div>
  </div>
</section>

<section class="piece dark card card-front">
  <div class="brand on-dark"><span class="dot"></span>Quorbeam</div>
</section>

<section class="piece dark notebook">
  <div class="faint-circle"></div>
  <div class="spiral">
    <span></span><span></span><span></span><span></span><span></span><span></span><span></span><span></span><span></span><span></span><span></span><span></span><span></span><span></span><span></span><span></span><span></span><span></span><span></span><span></span>
  </div>
  <div class="brand on-dark"><span class="dot"></span>Quorbeam</div>
</section>

<div class="keyring"></div>
<section class="piece paper keychain">
  <div class="brand on-light"><span class="dot"></span>Quorbeam</div>
</section>

<div class="pencil pencil-one"></div>
<div class="pencil pencil-two"></div>

<section class="piece dark eraser">
  <div class="brand on-dark"><span class="dot"></span>Quorbeam</div>
</section>

</body>
</html>
```